Marisella Crowe Photography

I am looking for someone to design a business card for me. I am a newborn and children's photographer. I want the card to have the proper contact information on it, but I want it to have a soft, simplistic, dreamy type of feel to attract moms. I would love to include soft colors. Maybe lavenders or pinks etc...

I have already had the logo designed and would like it incorporated into my business card.

I have uploaded a couple of the photo's I would like to use on the card. Feel free to use just one or both of them. Or however you see fit. The most important thing is for the card to have the feel i am looking for.

Thank you!

Target Market(s)

families and pregnant women looking for photography services.

Industry/Entity Type

Business

Font styles to use
Sans Serif
Other font styles liked:
• whatever fonts look light and whimsy, but easy to read

Colors
8869ae
eea4c8
86cae6
d2a4cc
e34197
86cfc6

Requirements
Must have
• www.marisellacrowephotography-example.com
www.facebook.com/marisellacrowephotography
marisella@marisellacrowephotography-example.com
555-392-1846
Should not have
• any masculine components i.e. dark colors, square boxes etc...

```html
<!DOCTYPE html>
<html lang="en">
<head>
<meta charset="utf-8">
<title>Marisella Crowe Photography — Business Card</title>
<link rel="stylesheet" href="https://fonts.googleapis.com/css2?family=Quicksand:wght@500&display=swap">
<style>
  :root {
    --page: #efedf2;
    --lavender: #8869ae;
    --lilac: #d2a4cc;
    --pink: #eea4c8;
    --blush: #f4c9d6;
    --peach: #f6c7b8;
    --cream: #f3ecc8;
    --ink: #6f4fa0;
  }
  * { box-sizing: border-box; margin: 0; padding: 0; }
  html, body {
    width: 1200px; height: 1000px; overflow: hidden;
    background: var(--page);
    font-family: "Quicksand", "Helvetica Neue", Arial, sans-serif;
  }
  .sheet {
    width: 1200px; height: 1000px;
    display: flex; flex-direction: column; align-items: center; justify-content: center;
    gap: 60px;
  }
  .card {
    position: relative;
    width: 700px; height: 400px;
    border-radius: 6px;
    overflow: hidden;
    box-shadow: 0 6px 20px rgba(90, 60, 120, 0.18);
  }
  .brand-name {
    font-size: 28px;
    font-weight: 500;
    color: var(--ink);
    letter-spacing: 0.5px;
    white-space: nowrap;
  }

  /* Front */
  .card-front .photo-area {
    position: absolute; left: 0; top: 0; width: 100%; height: 300px;
    background:
      radial-gradient(ellipse at 60% 55%, var(--peach) 0%, rgba(246,199,184,0) 55%),
      linear-gradient(100deg, var(--cream) 0%, var(--blush) 40%, var(--peach) 100%);
  }
  .card-front .brand-band {
    position: absolute; left: 0; bottom: 0; width: 100%; height: 100px;
    background: linear-gradient(90deg, var(--lavender) 0%, var(--lilac) 35%, #e2b6dc 55%, var(--lilac) 75%, var(--lavender) 100%);
    display: flex; align-items: center; padding-left: 110px;
  }

  /* Back */
  .card-back {
    background: linear-gradient(160deg, var(--lavender) 0%, #c69bd0 30%, var(--pink) 55%, #c9a0d4 80%, var(--lavender) 100%);
  }
  .card-back .keepsake-photo {
    position: absolute; right: 40px; top: 120px; width: 330px; height: 240px;
    border-radius: 50%;
    background: radial-gradient(ellipse at center, rgba(246,190,210,0.55) 0%, rgba(238,164,200,0) 70%);
  }
  .card-back .brand-name {
    position: absolute; right: 50px; top: 42px;
  }
  .contact-list {
    position: absolute; left: 48px; top: 120px;
    list-style: none;
    color: var(--ink);
    font-size: 19px; font-weight: 500;
    line-height: 34px;
  }
  .contact-list li { display: flex; align-items: center; gap: 10px; white-space: nowrap; }
  .contact-list svg { width: 18px; height: 18px; flex: none; }
  .tagline {
    position: absolute; left: 48px; bottom: 48px;
    color: var(--ink);
    font-size: 21px; font-weight: 500;
    white-space: nowrap;
  }
</style>
</head>
<body>
<main class="sheet">

  <section class="card card-front" aria-label="Card front">
    <div class="photo-area" role="img" aria-label="Photograph of a sleeping curly-haired baby on a soft pink patterned blanket"></div>
    <div class="brand-band">
      <span class="brand-name">Marisella Crowe Photography</span>
    </div>
  </section>

  <section class="card card-back" aria-label="Card back">
    <div class="keepsake-photo" role="img" aria-label="Faint photograph of a newborn with a rose, blended into the background"></div>
    <span class="brand-name">Marisella Crowe Photography</span>
    <ul class="contact-list">
      <li>
        <svg viewBox="0 0 18 18" aria-hidden="true"><circle cx="9" cy="9" r="7" fill="none" stroke="var(--ink)" stroke-width="1.6"/><path d="M2 9h14M9 2c3 3 3 11 0 14M9 2c-3 3-3 11 0 14" fill="none" stroke="var(--ink)" stroke-width="1.2"/></svg>
        www.marisellacrowephotography-example.com
      </li>
      <li>
        <svg viewBox="0 0 18 18" aria-hidden="true"><circle cx="9" cy="9" r="7.5" fill="var(--ink)"/></svg>
        marisellacrowephotography
      </li>
      <li>
        <svg viewBox="0 0 18 18" aria-hidden="true"><rect x="1.5" y="4" width="15" height="10" rx="1.5" fill="none" stroke="var(--ink)" stroke-width="1.6"/><path d="M2 5l7 5 7-5" fill="none" stroke="var(--ink)" stroke-width="1.4"/></svg>
        marisella@marisellacrowephotography-example.com
      </li>
      <li>
        <svg viewBox="0 0 18 18" aria-hidden="true"><path d="M5 2c-1.5.5-3 2-2.5 4.5C3.5 11 7 14.5 11.5 15.5c2.5.5 4-1 4.5-2.5l-3-2-1.5 1.5C9.5 11.5 6.5 8.5 6 6.5L7.5 5z" fill="var(--ink)"/></svg>
        555-392-1846
      </li>
    </ul>
    <p class="tagline">Specializing in Newborn and Children's Photography</p>
  </section>

</main>
</body>
</html>
```